Asphalt Driveway Billboard Design

We need a billboard designed for an Asphalt & Concrete Company in Minnesota. We want to advertise Asphalt Driveways on this billboard! Logo is uploaded below. Our website is pinecrest-paving.net for more information.

```html
<!DOCTYPE html>
<html lang="en">
<head>
<meta charset="utf-8">
<title>Pinecrest Paving Billboard</title>
<link href="https://fonts.googleapis.com/css2?family=Montserrat:wght@500;600;700;800;900&display=swap" rel="stylesheet">
<style>
  :root {
    --brand-blue: #0b76b9;
    --band-blue: #0a62a6;
    --deep-teal: #195b7d;
    --ink: #000000;
    --paper: #ffffff;
    --stage: #ececec;
  }
  html, body {
    margin: 0;
    padding: 0;
    width: 1200px;
    height: 960px;
    overflow: hidden;
    background: var(--stage);
  }
  .billboard {
    position: absolute;
    left: 40px;
    top: 321px;
    width: 1120px;
    height: 318px;
    box-shadow: 0 14px 30px rgba(0,0,0,0.25);
  }
  .billboard text { font-family: 'Montserrat', sans-serif; }
  .headline-small { font-weight: 500; font-size: 64px; fill: var(--paper); letter-spacing: 1px; }
  .headline-large { font-weight: 900; font-size: 100px; fill: var(--paper); }
  .service-label { font-weight: 700; font-size: 33px; fill: var(--paper); }
  .cta { font-weight: 700; font-size: 30px; fill: var(--paper); }
  .cta-free { font-size: 44px; font-weight: 800; }
  .brand-name { font-weight: 800; font-size: 58px; fill: var(--ink); letter-spacing: 2px; }
  .phone-number { font-weight: 900; font-size: 60px; fill: var(--ink); }
  .website { font-weight: 500; font-size: 38px; fill: var(--paper); }
</style>
</head>
<body>
<svg class="billboard" viewBox="0 0 1980 563" xmlns="http://www.w3.org/2000/svg" role="group" aria-label="Pinecrest Paving billboard">
  <!-- background panels -->
  <rect class="panel-black" x="0" y="0" width="1980" height="563" fill="var(--ink)"/>
  <polygon class="panel-teal-corner" points="1910,0 1980,0 1980,240 1900,350 1860,330" fill="var(--deep-teal)"/>
  <path class="panel-teal-sweep" d="M1780,330 Q1900,300 1980,310 L1980,360 Q1900,350 1800,380 Z" fill="var(--deep-teal)"/>
  <path class="panel-teal-sweep" d="M1860,455 Q1920,420 1980,410 L1980,440 Q1930,445 1880,470 Z" fill="var(--deep-teal)"/>
  <polygon class="panel-teal-foot" points="1640,525 1800,525 1778,563 1612,563" fill="var(--deep-teal)"/>
  <polygon class="panel-blue-stripe" points="432,0 562,0 790,563 700,563" fill="var(--brand-blue)"/>
  <polygon class="panel-white" points="0,0 432,0 747,497 0,497" fill="var(--paper)"/>
  <polygon class="panel-web-band" points="0,497 747,497 774,563 0,563" fill="var(--band-blue)"/>

  <!-- headline frame -->
  <polygon class="headline-frame" points="702,76 1850,76 1934,295 790,295" fill="none" stroke="var(--paper)" stroke-width="9"/>
  <rect class="quality-seal" x="1722" y="58" width="232" height="84" rx="6" fill="var(--band-blue)" stroke="#2a8ee0" stroke-width="4"/>
  <rect class="quality-seal-block" x="1722" y="58" width="88" height="84" rx="6" fill="#1565b4" stroke="#2a8ee0" stroke-width="4"/>

  <text class="headline-small" x="1317" y="160" text-anchor="middle">SERVING ALL YOUR</text>
  <text class="headline-large" x="1317" y="254" text-anchor="middle">ASPHALT NEEDS</text>

  <!-- services -->
  <polygon class="service-tag" points="867,325 1315,325 1330,370 882,370" fill="var(--brand-blue)"/>
  <polygon class="service-tag" points="1354,325 1802,325 1817,370 1369,370" fill="var(--brand-blue)"/>
  <polygon class="service-tag" points="902,393 1395,393 1410,438 917,438" fill="var(--brand-blue)"/>
  <polygon class="service-tag" points="1442,393 1787,393 1802,438 1457,438" fill="var(--brand-blue)"/>
  <text class="service-label" x="1099" y="360" text-anchor="middle">ASPHALT DRIVEWAYS</text>
  <text class="service-label" x="1586" y="360" text-anchor="middle">ASPHALT ADDITIONS</text>
  <text class="service-label" x="1157" y="428" text-anchor="middle">ASPHALT SEALCOATING</text>
  <text class="service-label" x="1620" y="428" text-anchor="middle">GARAGE FLOORS</text>

  <text class="cta" x="1394" y="508" text-anchor="middle">CALL FOR YOUR <tspan class="cta-free">FREE</tspan> ASPHALT ESTIMATE</text>

  <!-- brand block -->
  <circle class="brand-mark" cx="319" cy="150" r="78" fill="var(--brand-blue)"/>
  <text class="brand-name" x="319" y="310" text-anchor="middle">PINECREST</text>
  <text class="brand-name" x="319" y="372" text-anchor="middle">PAVING</text>

  <!-- phone -->
  <g class="phone-icon" transform="translate(102,445)">
    <circle r="24" fill="none" stroke="var(--ink)" stroke-width="3"/>
    <path d="M-9,-11 L-4,-13 L0,-5 L-3,-2 Q0,4 4,6 L7,3 L14,7 L12,12 Q2,14 -6,5 Q-13,-3 -9,-11 Z" fill="none" stroke="var(--ink)" stroke-width="2.4" stroke-linejoin="round"/>
  </g>
  <text class="phone-number" x="136" y="467">612-555-0148</text>

  <!-- website -->
  <g class="web-icon" transform="translate(135,523)">
    <circle r="16" fill="none" stroke="var(--paper)" stroke-width="2.5"/>
    <ellipse rx="7" ry="16" fill="none" stroke="var(--paper)" stroke-width="2"/>
    <line x1="-16" y1="0" x2="16" y2="0" stroke="var(--paper)" stroke-width="2"/>
  </g>
  <text class="website" x="160" y="536">pinecrest-paving.net</text>
</svg>
</body>
</html>
```